Stationery Design Project

We need a stationery design for our Norwegian trucking company. We have existed for about 15 years and our 12 drivers uses relatively new vehicles to transport goods around in northern Norway. Long distance routes with fresh fish og food transport is our main operations.

We have already made alogo that's printed on our trucks. The logo and a picture of our trucks is attached. I think the logo i crappy, but since its already in use, changing it is not an option in this round. Still using a better colour scheme in the overall stationery and more interesting fonts is possible (altso in the logo).

Company details:
Name: Vikmarka AS
Organisation nr 983 517 608
Post adress: 8640 Brekka

I like minimalism and simplicity. I am avalibly for questions in normal GMT working hours either here or on mail: kjell@brekkafrakt.no

Reason: Hi. Im extending the deadline because I needed some time to find a vector file of our logo. Sorry for the inconvenience

Hi, and thanks for all your interest in the project. Some updates:

-          I have decided to commit to using one of the designs. Some designer will get the payment.

-          I have extended the deadline with 24 hours since I needed some time to find our firms vector logo (a slow Swedish man was holding me up)

-          We will not choose a design before the deadline. No need to rush.

-          We have received a lot of great design and think there is a need to specified the product we want to make:

o   Business Card for all our employers. I just need the design and will duplicate with the correct numbers and name myself. The information on should be: Logo, employer’s name, Phone number, email, website, Postal number and address. Use this as a template: logo, Leif Dahlberg, 47382950, Leif@brekkafrakt.no,, brekkafrakt.no, 8640 Brekka. The order and placement of the information is your creative decision.

o   Stickers to put on the goods we travel. On the sticker the should be the following information: Logo, phone number, Tekst and link: Fraktæ av Vikmarka. Ke du syns? Brekkafrakt.no/tilbakemelding (this means: Handled by Vikmarka. What do you think Brekkafrakt.no/feedback -à the link will be a feedback form). The placement the information and size is your creative decision with some stings: we have been thinking of using Prentolo for printing and see that a size about 6x6 cm, 8x5 or something like that. (with 3000 copies our budget is 200 punds). Any suggestions of other suppliers are welcome. Prentolo price calculator http://www.prentoloprints.example/digital-litho-printing/printing-labels-tags/stickers/

o   Letterhead with logo, address, phone number and organizational number.

o   Envelopes with logo,address, phone number and organizational number.

Have a nice day.

 

 

• Using the blue colour in the logo and using a similar graphic approch.

```html
<!DOCTYPE html>
<html lang="no">
<head>
<meta charset="utf-8">
<title>Vikmarka AS – Stationery</title>
<link href="https://fonts.googleapis.com/css2?family=Arimo:wght@400;700&display=swap" rel="stylesheet">
<style>
  :root {
    --violet: #3f14a0;
    --green: #5cbf2a;
    --ink: #333;
    --board: #e8e8e8;
    --paper: #fff;
    --edge: #8a8a8a;
  }
  * { box-sizing: border-box; margin: 0; padding: 0; }
  html, body { width: 1200px; height: 834px; overflow: hidden; }
  body { background: var(--board); font-family: "Arimo", Arial, sans-serif; color: var(--ink); position: relative; }
  .board-frame { position: absolute; left: 10px; top: 10px; width: 1180px; height: 814px; border: 2px solid #f7f7f7; border-radius: 8px; }
  .label { position: absolute; font-size: 19px; color: #222; }
  .sheet { position: absolute; background: var(--paper); border: 1px solid var(--edge); overflow: hidden; }
  .sheet svg.accent { position: absolute; left: 0; top: 0; }
  .wordmark { position: absolute; display: flex; align-items: center; gap: 6px; font-weight: 700; color: var(--violet); white-space: nowrap; }
  .wordmark .dot { border-radius: 50%; background: var(--green); flex: none; }
  .address { position: absolute; color: var(--violet); line-height: 1.2; white-space: nowrap; }

  /* sticker */
  .sticker { position: absolute; left: 246px; top: 59px; width: 158px; height: 158px; }
  .sticker .wordmark { left: 39px; top: 70px; font-size: 15px; gap: 4px; }
  .sticker .wordmark .dot { width: 10px; height: 10px; }

  /* envelope */
  .envelope { left: 56px; top: 234px; width: 532px; height: 264px; }
  .envelope .wordmark { left: 52px; top: 118px; font-size: 24px; }
  .envelope .wordmark .dot { width: 15px; height: 15px; }
  .envelope .address { left: 53px; top: 173px; font-size: 11px; }

  /* letterhead */
  .letterhead { left: 620px; top: 53px; width: 440px; height: 716px; }
  .letterhead .wordmark { left: 76px; top: 40px; font-size: 28px; }
  .letterhead .wordmark .dot { width: 17px; height: 17px; }
  .letter-body { position: absolute; left: 78px; top: 163px; width: 337px; font-size: 7.6px; line-height: 10px; text-align: justify; }
  .letter-body p { margin-bottom: 10px; }
  .signature { width: 70px; height: 30px; background: #eee; margin-top: -4px; }
  .letterhead .address { left: 298px; top: 640px; font-size: 9.5px; }

  /* business card */
  .card { width: 206px; height: 133px; }
  .card-front { left: 90px; top: 534px; }
  .card-back { left: 320px; top: 534px; }
  .card-front .wordmark { left: 96px; top: 13px; font-size: 11px; gap: 3px; }
  .card-front .wordmark .dot { width: 7px; height: 7px; }
  .holder-name { position: absolute; left: 16px; top: 58px; font-size: 10px; color: var(--green); }
  .holder-role { position: absolute; left: 16px; top: 70px; font-size: 7px; color: var(--violet); }
  .card-front .address { left: 100px; top: 95px; font-size: 5px; line-height: 6.4px; }
  .card-back .wordmark { left: 46px; top: 52px; font-size: 17px; gap: 4px; }
  .card-back .wordmark .dot { width: 11px; height: 11px; }
</style>
</head>
<body>
  <div class="board-frame"></div>

  <div class="label" style="left:152px;top:108px">sticker</div>
  <div class="label" style="left:516px;top:58px">letterhead</div>
  <div class="label" style="left:74px;top:197px">DL envelope</div>
  <div class="label" style="left:74px;top:512px">card front</div>
  <div class="label" style="left:390px;top:512px">back</div>

  <div class="sticker">
    <svg width="158" height="158" viewBox="0 0 158 158">
      <circle cx="79" cy="79" r="79" fill="var(--green)"/>
      <circle cx="79" cy="79" r="60" fill="var(--paper)"/>
      <defs>
        <path id="ring-path" d="M 79 79 m -69 0 a 69 69 0 1 1 138 0 a 69 69 0 1 1 -138 0"/>
      </defs>
      <text font-family="Arimo, Arial, sans-serif" font-size="8.4" font-weight="700" fill="#fff">
        <textPath href="#ring-path" startOffset="2%">Fraktæ av Vikmarka. Ke du syns? • Tlf 47382950 • www.brekkafrakt.no/tilbakemelding</textPath>
      </text>
    </svg>
    <div class="wordmark"><span class="dot"></span>Vikmarka</div>
  </div>

  <div class="sheet envelope">
    <svg class="accent" width="532" height="264" viewBox="0 0 532 264">
      <rect x="38" y="0" width="3" height="70" fill="var(--violet)"/>
      <circle cx="39.5" cy="78" r="3" fill="var(--green)"/>
      <circle cx="262" cy="183.5" r="3" fill="var(--green)"/>
      <rect x="270" y="182" width="262" height="3" fill="var(--violet)"/>
    </svg>
    <div class="wordmark"><span class="dot"></span>Vikmarka</div>
    <div class="address">
      Vikmarka AS<br>
      Organisation nr 983 517 608<br>
      8640 Brekka - Norge<br>
      Tel. 0456 78 901 234<br>
      www.brekkafrakt.no
    </div>
  </div>

  <div class="sheet letterhead">
    <svg class="accent" width="440" height="716" viewBox="0 0 440 716">
      <rect x="424" y="0" width="3" height="110" fill="var(--violet)"/>
      <circle cx="425.5" cy="118" r="3" fill="var(--green)"/>
      <rect x="0" y="646" width="250" height="3" fill="var(--violet)"/>
      <circle cx="258" cy="647.5" r="3" fill="var(--green)"/>
    </svg>
    <div class="wordmark"><span class="dot"></span>Vikmarka</div>
    <div class="letter-body">
      <p>Lorem ipsum dolor</p>
      <p>Sit amet, consectetur adipiscing elit. Sed justo dui, mollis sed hendrerit ut, sagittis eu tellus. Maecenas pellentesque orci vel ante ullamcorper sed luctus sem feugiat. Nunc auctor malesuada lacus, a lacinia tellus venenatis ac. Cum sociis natoque penatibus et magnis dis parturient montes, nascetur ridiculus mus. Etiam in imperdiet tortor. Vestibulum vestibulum nibh vitae enim adipiscing imperdiet sit amet non arcu. In hac habitasse platea dictumst. Nam massa augue, pulvinar ac sollicitudin elementum, rutrum vel turpis. Morbi hendrerit, magna ut placerat fringilla, odio arcu auctor risus, eu scelerisque ante tellus quis eros. Sed id consequat justo. Curabitur lacinia metus et purus laoreet in imperdiet sapien pretium. Donec sit amet iaculis augue. Donec vel augue nec ipsum interdum molestie. Nullam non lectus metus, vel sodales sem.</p>
      <p>Maecenas aliquet pulvinar nisl sit amet elementum. Nam velit massa, elementum eu cursus vel, congue vel quam. Mauris in diam viverra massa rutrum cursus. Nulla lacinia justo non mi pulvinar euismod. Cum sociis natoque penatibus et magnis dis parturient montes, nascetur ridiculus mus. Aliquam placerat accumsan tellus, nec euismod nibh vulputate eget. Quisque sollicitudin ultrices malesuada. In quis nisl tincidunt arcu iaculis feugiat.</p>
      <p>Donec ut ultrices urna. Vestibulum dignissim porttitor laoreet. Nunc gravida tincidunt venenatis. Etiam hendrerit arcu ac quam luctus a mattis nunc eleifend. Fusce ac interdum elit. Maecenas fermentum elit sit amet diam sodales vitae molestie arcu sodales. Aliquam non arcu sapien. Cum sociis natoque penatibus et magnis dis parturient montes, nascetur ridiculus mus. Integer eu sapien magna. Vestibulum aliquam tristique sem, in convallis arcu facilisis in. Sed sapien leo, aliquet vel accumsan eget, dapibus eget ligula.</p>
      <p>Aliquam euismod, nisl quis</p>
      <p>Cras pharetra<br>&nbsp;pretium enim,</p>
      <div class="signature" role="img" aria-label="Handwritten signature"></div>
    </div>
    <div class="address">
      Vikmarka AS<br>
      Organisation nr 983 517 608<br>
      8640 Brekka - Norge<br>
      Tel. 0456 78 901 234<br>
      www.brekkafrakt.no
    </div>
  </div>

  <div class="sheet card card-front">
    <svg class="accent" width="206" height="133" viewBox="0 0 206 133">
      <rect x="0" y="96" width="84" height="2" fill="var(--violet)"/>
      <circle cx="89" cy="97" r="2" fill="var(--green)"/>
    </svg>
    <div class="wordmark"><span class="dot"></span>Vikmarka</div>
    <div class="holder-name">Leif DAHLBERG</div>
    <div class="holder-role">Company Position</div>
    <div class="address">
      Vikmarka AS<br>
      8640 Brekka - Norge<br>
      Tel. 47382950<br>
      leif@brekkafrakt.no<br>
      www.brekkafrakt.no
    </div>
  </div>

  <div class="sheet card card-back">
    <svg class="accent" width="206" height="133" viewBox="0 0 206 133">
      <rect x="186" y="0" width="2" height="52" fill="var(--violet)"/>
      <circle cx="187" cy="57" r="2" fill="var(--green)"/>
    </svg>
    <div class="wordmark"><span class="dot"></span>Vikmarka</div>
  </div>
</body>
</html>
```